Massage Therapy and Energy Healing Practice

I am a massage therapist, Reiki energy healer, I sell herbs and oils, and also a health lifestyle coach. I need a design that is strong because I'm not a spa. I do therapeutic work, but I want a touch of the energy and spiritual healing I do as well to be included in the design. I like blue, green, or purple colors. I live in the Blue Ridge Mountains of VA and even though my practice is in the city I like my love for nature and the earth to show through. I would like a single image logo so I can use the image many places. I need a strong brand that will let others know that I combine massage therapy in a therapeutic way while keeping my touches of energy healing, nurturing, herb crafting, and mother earth loving ways.
Updates

Just some things about me:I like to hike. I live on a farm. I own horses, cows, sheep and dogs. I love nature and the energy in produces. I'm very spiritual. I don't know how these things might help or if they do, but I know that my personality might help inspire what I will find good in a design. Added Sunday, December 13, 2015

Target Market(s)

People in pain. People who need spiritual council. Need herbal medicine advice. Holistic healthcare.

Industry/Entity Type

Massage

Contact Information for Business Card

Kneadwell Harbor
Norah T. Lindqvist C.M.T, R.M.T
40913 Hollister Creek Court, Dunmore, VA
540-718-2263

Colors
3176b5
85abd2
876aae
9bcb3c

Requirements
Must have
• Strong Branding that promotes my massage therapy practice first
Nice to have
• Something to evoke my herbal medicine, my energy healing, my spiritual side

```html
<!DOCTYPE html>
<html lang="en">
<head>
<meta charset="utf-8">
<title>Kneadwell Harbor — Business Card</title>
<link rel="stylesheet" href="https://fonts.googleapis.com/css2?family=Crimson+Text:ital,wght@1,600&family=Open+Sans:wdth,wght@75,400&family=Quicksand:wght@400&family=Yellowtail&family=Josefin+Sans:wght@400&display=swap">
<style>
  :root {
    --page: #ffffff;
    --leaf-dark: #2f7d2a;
    --leaf: #4faa38;
    --glow: #d6e22a;
    --meadow: #7aa82c;
    --meadow-deep: #3a6a1c;
    --bloom: #f0c81e;
    --plum: #8a3e9c;
    --white: #ffffff;
    --ink: #111111;
  }
  * { margin: 0; padding: 0; box-sizing: border-box; }
  html, body {
    width: 1200px;
    height: 1000px;
    overflow: hidden;
    background: var(--page);
  }
  .canvas {
    position: relative;
    width: 1200px;
    height: 1000px;
  }
  .card {
    position: absolute;
    left: 194px;
    top: 220px;
    width: 830px;
    height: 455px;
    overflow: hidden;
  }
  .meadow-photo {
    position: absolute;
    inset: 0 0 38px 0;
    background:
      radial-gradient(ellipse 38% 26% at 50% 22%, rgba(214,226,42,0.95), rgba(214,226,42,0) 75%),
      radial-gradient(ellipse 30% 30% at 0% 0%, rgba(47,125,42,0.9), rgba(47,125,42,0) 80%),
      radial-gradient(ellipse 30% 30% at 100% 0%, rgba(47,125,42,0.9), rgba(47,125,42,0) 80%),
      radial-gradient(ellipse 14% 9% at 18% 82%, rgba(240,200,30,0.85), rgba(240,200,30,0) 80%),
      radial-gradient(ellipse 12% 8% at 57% 74%, rgba(240,200,30,0.85), rgba(240,200,30,0) 80%),
      radial-gradient(ellipse 14% 9% at 88% 72%, rgba(240,200,30,0.8), rgba(240,200,30,0) 80%),
      radial-gradient(ellipse 70% 22% at 50% 86%, rgba(240,200,30,0.45), rgba(240,200,30,0) 80%),
      linear-gradient(180deg, var(--leaf-dark) 0%, var(--leaf) 14%, #b4d82e 36%, #8fbf2c 52%, var(--meadow) 66%, var(--meadow-deep) 100%);
  }
  .phone {
    position: absolute;
    left: 14px;
    top: 12px;
    display: flex;
    align-items: center;
    gap: 3px;
    color: var(--white);
    font-family: "Open Sans", "Arial Narrow", sans-serif;
    font-stretch: 75%;
    font-weight: 400;
    font-size: 31px;
    line-height: 1;
  }
  .phone svg { width: 26px; height: 30px; }
  .therapist {
    position: absolute;
    right: 27px;
    top: 4px;
    text-align: right;
  }
  .therapist-name {
    color: var(--white);
    font-family: "Crimson Text", Georgia, serif;
    font-style: italic;
    font-weight: 600;
    font-size: 39px;
    line-height: 1.1;
  }
  .credentials {
    color: var(--ink);
    font-family: "Josefin Sans", Arial, sans-serif;
    font-weight: 400;
    font-size: 19px;
    line-height: 1;
    margin-right: 102px;
    margin-top: -2px;
  }
  .brand-name {
    position: absolute;
    left: 0;
    right: 0;
    top: 132px;
    text-align: center;
    padding-left: 12px;
    color: var(--plum);
    font-family: "Yellowtail", cursive;
    font-weight: 400;
    font-size: 86px;
    line-height: 1;
  }
  .address-band {
    position: absolute;
    left: 0;
    right: 0;
    bottom: 0;
    height: 38px;
    background: var(--plum);
    color: var(--white);
    font-family: "Quicksand", Arial, sans-serif;
    font-weight: 400;
    font-size: 29px;
    letter-spacing: 3px;
    line-height: 38px;
    text-align: center;
    white-space: nowrap;
  }
</style>
</head>
<body>
<div class="canvas">
  <section class="card">
    <div class="meadow-photo" role="img" aria-label="Photo of a sunlit meadow with yellow buttercups and daisies under overhanging green leaves"></div>

    <div class="phone">
      <svg viewBox="0 0 24 28" aria-hidden="true">
        <path fill="#ffffff" d="M6 2c1-.6 2-.3 2.6.6l2.2 4c.5.9.2 1.9-.6 2.5l-1.6 1.1c.9 2.8 2.4 5.4 4.4 7.5l1.7-.9c.9-.5 2-.2 2.5.6l2.5 3.8c.5.9.3 2-.5 2.6l-2 1.4c-1.3.9-3 .9-4.3 0C7 21.3 3.2 14.9 2.6 7.8 2.5 6.3 3.2 4.8 4.4 3.9z"/>
      </svg>
      <span>540-718-2263</span>
    </div>

    <div class="therapist">
      <div class="therapist-name">Norah T. Lindqvist</div>
      <div class="credentials">C.M.T, R.M.T</div>
    </div>

    <h1 class="brand-name">Kneadwell Harbor</h1>

    <div class="address-band">40913 Hollister Creek Court, Dunmore, VA</div>
  </section>
</div>
</body>
</html>
```